New high end server provider needs wordpress design

www.kv7hostrack.com

Need a wordpress design for a high end server provider that provides overclocked dedicated servers for rent. We are located in Chicago but we have a presence is Virginia and Nevada for both our east and west coast customers.

We are a server provider that specializes in top end hardware with every feature designed for optimum performance. If it is not the best quality part or provides the best possible performance we don't run it. Our customers are mainly those that want the best single threaded performance possible from their hardware. We would be selling our services directly on our website via WHMCS.

We would like to see designs that are very modern and simplistic yet very attractive looking and catchy. Would prefer colors in the blues and greens and white. These colors are not necessary and I would be open to another color scheme if it looks good.

The final design should show speed and performance while being simplistic and easy on the eyes.
Updates

Logo and company name added and payment changed to guaranteed.  Looking for a wordpress template with the same pages as kv7hostrack.com but with a redesigned look and feel.  

WHMCS control panel design also part of the design request.

If you have any questions please let me know!  This is just for kv7hostrack.com and a main page for WHMCS (no coding just design).

Target Market(s)

IT Guru's (mostly men in their 20's to 30's)

Industry/Entity Type

Hardware

Requirements
Must have
• WHMCS panel design to fit with website theme.
Nice to have
• Main slider on home page similar to one of our other websites at www.kv7hostrack.com
Should not have
• Flash or frames

```html
<!DOCTYPE html>
<html lang="en">
<head>
<meta charset="utf-8">
<title>KV7HostRack – Overclocked Dedicated Servers</title>
<link rel="stylesheet" href="https://fonts.googleapis.com/css2?family=Arimo:wght@400;700&display=swap">
<style>
:root{
  --page:#f3f4f5;
  --nav:#1e3a44;
  --navline:#5d7a84;
  --blue:#2f9fcf;
  --blue-dark:#1f7fa8;
  --feed:#3d9fc4;
  --strip:#0f3d6e;
  --text:#6a6a6a;
  --dark:#222;
  --footer:#3b3b3b;
  --footer-bar:#111;
  --tab:#e2e2e2;
  --border:#d6d6d6;
  --white:#fff;
}
*{box-sizing:border-box;margin:0;padding:0}
html,body{width:1200px;height:2175px;overflow:hidden}
body{background:var(--page);font-family:"Arimo",Arial,sans-serif;color:var(--text);position:relative}
.abs{position:absolute}

/* header */
.topnav{left:382px;top:0;width:806px;height:55px;background:var(--nav);display:flex;align-items:center;justify-content:space-around;padding:0 14px;border-radius:0 0 0 4px}
.topnav a{color:var(--white);text-decoration:none;font-size:14px}
.topnav .sep{width:1px;height:16px;background:var(--navline)}
.brand{left:22px;top:52px;font-size:30px;font-weight:700;color:var(--nav);line-height:36px}
.info{top:90px;display:flex;align-items:center;gap:10px;font-size:14px;color:var(--dark)}
.search{left:932px;top:80px;width:248px;height:40px;background:var(--white);border:1px solid var(--border);border-radius:3px;display:flex;align-items:center;justify-content:space-between;padding:0 12px;font-size:17px;color:#888}

/* hero */
.hero{left:12px;top:142px;width:1178px;height:376px;box-shadow:0 30px 30px -18px rgba(0,0,0,.55)}
.hero-tabs{position:absolute;left:0;top:0;width:146px;height:100%;background:var(--strip);display:flex}
.hero-tabs div{flex:1;border-right:1px solid #3c6f9a;display:flex;align-items:center;justify-content:center}
.hero-tabs span{writing-mode:vertical-rl;transform:rotate(180deg);color:var(--white);font-size:14px;white-space:nowrap}
.hero-photo{position:absolute;left:146px;top:0;right:0;bottom:0;background:radial-gradient(circle at 55% 40%,#2b2b2b 0,#1b1b1b 22%,#3a6c9a 45%,#274a74 70%,#1d3552 100%)}

.intro{left:18px;top:598px;width:1165px;font-size:19px;line-height:28px;color:#666}
.intro b{color:var(--blue-dark);font-weight:400}

.section-title{left:14px;top:700px;font-size:21px;font-weight:700;color:var(--dark)}

/* tabs */
.tabs{left:12px;top:757px;width:1176px;height:46px;display:flex;gap:4px}
.tabs div{flex:1;background:var(--tab);display:flex;align-items:center;justify-content:center;font-size:14px;color:#555;border:1px solid var(--border)}
.tabs .active{background:var(--blue);color:var(--white);border-color:var(--blue)}
.tab-body{left:12px;top:803px;width:1176px;height:365px;background:var(--white);border:1px solid var(--border)}
.tab-img{left:25px;top:820px;width:158px;height:135px;background:linear-gradient(160deg,#dfe9f3,#9cbcd8 60%,#e8eef3)}
.tab-head{left:210px;top:822px;font-size:22px;line-height:27px;color:var(--blue);font-weight:400}
.tab-text{left:210px;top:895px;width:965px;font-size:13.6px;line-height:17.5px;text-align:justify;color:#777}
.btn{left:1032px;top:1115px;width:146px;height:34px;background:var(--blue-dark);color:var(--white);font-size:15px;display:flex;align-items:center;justify-content:center}

/* latest technology */
.latest{left:22px;top:1230px;font-size:34px;letter-spacing:1px;color:#999;font-weight:700}
.latest-icon{left:25px;top:1312px;width:118px;height:138px;background:linear-gradient(180deg,#d0d0d0,#8e8e8e)}
.latest-text{left:158px;top:1282px;width:525px;font-size:13.6px;line-height:17.5px;text-align:justify;color:#666}

.feed{left:692px;top:1232px;width:498px;height:313px;background:var(--feed);border-radius:3px;color:var(--white)}
.feed-head{display:flex;justify-content:space-between;align-items:center;padding:14px 12px 8px}
.feed-head h3{font-weight:400;font-size:20px}
.follow{display:flex;align-items:center;gap:6px}
.follow .f{background:var(--white);color:#333;font-size:13px;padding:4px 10px;border-radius:3px;font-weight:700}
.follow .n{background:var(--white);color:#666;font-size:11px;padding:4px 8px;border-radius:3px}
.feed-item{display:flex;align-items:flex-start;gap:30px;padding:16px 12px 14px 12px;border-top:1px solid rgba(255,255,255,.35);font-size:13.4px;line-height:18px}
.feed-item:first-of-type{border-top:none}

/* technology band */
.tech-band{left:0;top:1650px;width:1200px;height:113px;background:#2d2d2d}
.tech-label{left:10px;top:1652px;width:348px;height:109px;background:linear-gradient(180deg,#5cc2ec,#2c9fd3);border:2px solid var(--white);display:flex;align-items:center;justify-content:center;font-size:30px;font-weight:700;color:var(--dark)}
.partner{top:1654px;height:105px;background:var(--white);border:3px solid #222;display:flex;align-items:center;justify-content:center;font-size:26px;font-weight:700;color:#222}

/* footer */
.footer{left:0;top:1812px;width:1200px;height:313px;background:var(--footer);border-top:3px solid #777}
.fcol{top:1850px;color:#ddd}
.fcol h4{font-weight:400;font-size:19px;color:#bbb;margin-bottom:40px}
.fcol ul{list-style:none}
.fcol li{font-size:14px;height:33px;display:flex;align-items:center;gap:22px;color:var(--white)}
.fcol li.cur{text-decoration:underline}
.fcol p{font-size:13px;line-height:16px;color:#ddd;text-align:justify}
.contact li{gap:0}
.contact li b{font-weight:400;width:70px;display:inline-block}
.social{display:flex;gap:8px;margin-top:8px}
.social span{width:30px;height:30px;background:#7c9bb0;border-radius:3px}
.bottom{left:0;top:2125px;width:1200px;height:50px;background:var(--footer-bar);color:var(--white);font-size:15px}
.bottom .copy{position:absolute;left:232px;top:16px}
.bottom .links{position:absolute;left:830px;top:16px;display:flex;gap:22px}
</style>
</head>
<body>

<nav class="abs topnav">
  <a>Home</a><span class="sep"></span><a>About us</a><span class="sep"></span><a>Services</a><span class="sep"></span><a>Dedicated srrvers</a><span class="sep"></span><a>FAQ</a><span class="sep"></span><a>Contact us</a>
</nav>

<div class="abs brand">KV7HostRack</div>

<div class="abs info" style="left:540px">
  <svg width="22" height="22" viewBox="0 0 22 22"><circle cx="11" cy="11" r="10" fill="#4a9b3c"/><circle cx="11" cy="11" r="4" fill="#fff"/></svg>
  <span>info-name</span>
</div>
<div class="abs info" style="left:695px">
  <svg width="22" height="22" viewBox="0 0 22 22"><path d="M5 3h4l2 5-3 2a11 11 0 0 0 5 5l2-3 5 2v4a2 2 0 0 1-2 2A16 16 0 0 1 3 5a2 2 0 0 1 2-2z" fill="#222"/></svg>
  <span>000-(000)-0000</span>
</div>
<div class="abs search"><span>Search</span>
  <svg width="22" height="22" viewBox="0 0 22 22"><circle cx="9" cy="9" r="6.5" fill="none" stroke="#999" stroke-width="2"/><line x1="14" y1="14" x2="20" y2="20" stroke="#999" stroke-width="2.5"/></svg>
</div>

<section class="abs hero">
  <div class="hero-tabs">
    <div><span>Overclocked High Quality Hardware</span></div>
    <div><span>Speeds that set us apart from the competition</span></div>
    <div><span>Dedicated CPU core with high priority access</span></div>
    <div><span>VXCP Admin Panel</span></div>
  </div>
  <div class="hero-photo" role="img" aria-label="Close-up of a CPU cooler fan mounted on a blue server motherboard"></div>
</section>

<p class="abs intro">KV7HostRack offer the highest quality, highest performing Frontier <b>Siege 2 servers</b> available for rent. Our servers are custom built specifically for the demanding requirements of Frontier Siege 2 Beta.</p>

<h2 class="abs section-title">Why Customer chose us&nbsp; ?</h2>

<div class="abs tabs">
  <div class="active">Best performing fs2 server</div>
  <div>Dedicated Server design</div>
  <div>Best for game</div>
  <div>VXCP controle panal</div>
  <div>Built in FS2 web-admin panel</div>
</div>
<div class="abs tab-body"></div>
<div class="abs tab-img" role="img" aria-label="Illustration of people gathered around a computer screen"></div>
<h3 class="abs tab-head">Best performing Frontier Siege 2 servers<br>currently on the market.</h3>
<p class="abs tab-text">Sed ut perspiciatis unde omnis iste natus error sit voluptatem accusantium doloremque laudantium, totam rem aperiam, eaque ipsa quae ab illo inventore veritatis et quasi architecto beatae vitae dicta sunt explicabo. Nemo enim ipsam voluptatem quia voluptas sit aspernatur aut odit aut fugit, sed quia consequuntur magni dolores eos qui ratione voluptatem sequi nesciunt. Neque porro quisquam est, qui dolorem ipsum quia dolor sit amet, consectetur, adipisci velit, sed quia non numquam eius modi tempora incidunt ut labore et dolore magnam aliquam quaerat voluptatem. Ut enim ad minima veniam, quis nostrum exercitationem ullam corporis suscipit laboriosam, nisi ut aliquid ex ea commodi consequatur? Quis autem vel eum iure reprehenderit qui in ea voluptate velit esse quam nihil molestiae consequatur, vel illum qui dolorem eum fugiat quo voluptas nulla pariatur?"Sed ut perspiciatis unde omnis iste natus error sit voluptatem accusantium doloremque laudantium, totam rem aperiam, eaque ipsa quae ab illo inventore veritatis et quasi architecto beatae vitae dicta sunt explicabo. Nemo enim ipsam voluptatem quia voluptas sit aspernatur aut odit aut fugit, sed quia consequuntur magni dolores eos qui ratione voluptatem sequi nesciunt. Neque porro quisquam est, qui dolorem ipsum quia dolor sit amet, consectetur, adipisci velit.</p>
<div class="abs btn">Learn more</div>

<h2 class="abs latest">LATEST TECHNOLOGY</h2>
<div class="abs latest-icon" role="img" aria-label="Grey illustration of a computer with circuitry"></div>
<p class="abs latest-text">Sed ut perspiciatis unde omnis iste natus error sit voluptatem accusantium doloremque laudantium, totam rem aperiam, eaque ipsa quae ab illo inventore veritatis et quasi architecto beatae vitae dicta sunt explicabo. Nemo enim ipsam voluptatem quia voluptas sit aspernatur aut odit aut fugit, sed quia consequuntur magni dolores eos qui ratione voluptatem sequi nesciunt. Neque porro quisquam est, qui dolorem ipsum quia dolor sit amet, consectetur, adipisci velit, sed quia non numquam</p>

<aside class="abs feed">
  <div class="feed-head"><h3>Chirper Feed</h3><div class="follow"><span class="f">Follow</span><span class="n">1000 follower</span></div></div>
  <div class="feed-item"><svg width="22" height="22" viewBox="0 0 22 22" style="flex:none"><circle cx="11" cy="11" r="10" fill="#8fc5db"/><path d="M9 6l6 5-6 5z" fill="#3d9fc4"/></svg><span>We are in the process of expanding to the west coast. Look for our new location (California) to come online before KV7's release! 05:38:01 AM July 21, 2012 from web</span></div>
  <div class="feed-item"><svg width="22" height="22" viewBox="0 0 22 22" style="flex:none"><circle cx="11" cy="11" r="10" fill="#8fc5db"/><path d="M9 6l6 5-6 5z" fill="#3d9fc4"/></svg><span>We are in the process of expanding to the west coast. Look for our new location (California) to come online before KV7's release! 05:38:01 AM July 21, 2012 from web</span></div>
  <div class="feed-item"><svg width="22" height="22" viewBox="0 0 22 22" style="flex:none"><circle cx="11" cy="11" r="10" fill="#8fc5db"/><path d="M9 6l6 5-6 5z" fill="#3d9fc4"/></svg><span>We are in the process of expanding to the west coast. Look for our new location (California) to come online before KV7's release! 05:38:01 AM July 21, 2012 from web</span></div>
</aside>

<div class="abs tech-band"></div>
<div class="abs tech-label">Technology&nbsp; we use</div>
<div class="abs partner" style="left:375px;width:280px">Northwind Soft</div>
<div class="abs partner" style="left:662px;width:255px">Arvex</div>
<div class="abs partner" style="left:925px;width:265px">Coreline</div>

<footer class="abs footer"></footer>
<div class="abs fcol" style="left:18px;width:260px">
  <h4>Navigation</h4>
  <ul>
    <li class="cur"><svg width="10" height="12" viewBox="0 0 10 12"><path d="M5 0l5 6H6v6H4V6H0z" fill="#ccc"/></svg>Home</li>
    <li><svg width="10" height="12" viewBox="0 0 10 12"><path d="M5 0l5 6H6v6H4V6H0z" fill="#ccc"/></svg>Services</li>
    <li><svg width="10" height="12" viewBox="0 0 10 12"><path d="M5 0l5 6H6v6H4V6H0z" fill="#ccc"/></svg>About us</li>
    <li><svg width="10" height="12" viewBox="0 0 10 12"><path d="M5 0l5 6H6v6H4V6H0z" fill="#ccc"/></svg>Faq</li>
    <li><svg width="10" height="12" viewBox="0 0 10 12"><path d="M5 0l5 6H6v6H4V6H0z" fill="#ccc"/></svg>Contact us</li>
  </ul>
</div>
<div class="abs fcol" style="left:312px;width:280px">
  <h4>Services</h4>
  <ul>
    <li><svg width="14" height="14" viewBox="0 0 14 14"><circle cx="7" cy="7" r="5.5" fill="none" stroke="#ccc" stroke-width="2"/></svg>Dedicated server design</li>
    <li><svg width="14" height="14" viewBox="0 0 14 14"><circle cx="7" cy="7" r="5.5" fill="none" stroke="#ccc" stroke-width="2"/></svg>Best for all game slots</li>
    <li><svg width="14" height="14" viewBox="0 0 14 14"><circle cx="7" cy="7" r="5.5" fill="none" stroke="#ccc" stroke-width="2"/></svg>VXCP controle panal</li>
    <li><svg width="14" height="14" viewBox="0 0 14 14"><circle cx="7" cy="7" r="5.5" fill="none" stroke="#ccc" stroke-width="2"/></svg>Built in FS2 web-admin panel</li>
    <li style="align-items:flex-start;line-height:17px;height:40px"><svg width="14" height="14" viewBox="0 0 14 14" style="flex:none"><circle cx="7" cy="7" r="5.5" fill="none" stroke="#ccc" stroke-width="2"/></svg>Personal and dedicated<br>customer support.</li>
  </ul>
</div>
<div class="abs fcol" style="left:608px;width:285px">
  <h4>Testimonials</h4>
  <p style="margin-top:-2px">Sed ut perspiciatis unde omnis iste natus error sit voluptatem accusantium doloremque laudantium, totam rem aperiam, eaque ipsa quae ab illo inventore veritatis et quasi architecto beatae vitae dicta sunt explicabo. Nemo enim ipsam voluptatem quia voluptas sit aspernatur aut odit aut fugit, sed quia consequuntur magni dolores eos qui ratione voluptatem sequi nesciunt. Neque porro quisquam</p>
</div>
<div class="abs fcol contact" style="left:922px;width:270px">
  <h4>Our contact and links</h4>
  <ul>
    <li>Dana "Voltage"</li>
    <li><b>Phone:</b>+1 555-014-2290</li>
    <li><b>Email:</b>dana@kv7hostrack.com</li>
  </ul>
  <div style="font-size:18px;margin-top:10px">Follow us :</div>
  <div class="social"><span></span><span></span><span></span><span></span></div>
</div>

<div class="abs bottom">
  <span class="copy">Copyright ©2013 KV7 HostRack</span>
  <span class="links"><span>Privacy policy</span><span>|</span><span>Terms of use</span></span>
</div>

</body>
</html>
```